Math Tuition center needs a fresh website with LMS

I'm intending to buy a LMS theme for my wordpress site. But I need someone to help me design a few posters for the slider and set up the entire site for me. The LMS theme I'm eyeing has everything I need. But I don't have the time to figure things out.
I'm looking at either:
http://themes.brightpanel.com/smartlesson/
or
http://gallerydeck.org/vantor/
My current site is online at www.tallywise.com
I also need you to help me clear up the files I don't need on the server. So basically I need someone to design the new site for me, the LMS theme should make things easier but I'll need some customizations. I also need a webmaster who can help me set up the entire site so I don't have to turn on the widget or mess around with the theme.
Another thing, I have SEO done onsite so I can't change the contents, the meta-tags and such.
Industry/Entity Type
Online
Look and feel
Each slider illustrates characteristics of the customer's brand and the style your logo design should communicate.

```html
<!DOCTYPE html>
<html lang="en">
<head>
<meta charset="utf-8">
<title>tallywise — Math Tuition</title>
<link href="https://fonts.googleapis.com/css2?family=Noto+Serif:wght@400;700&family=Roboto+Condensed:wght@300;400;700&display=swap" rel="stylesheet">
<style>
:root{
  --green:#39a935;
  --green-hero:#3cb33a;
  --green-dark:#2e8f2b;
  --text:#5b5b5b;
  --heading:#555555;
  --muted:#8a8a8a;
  --grey-btn:#8d8d8d;
  --band:#f3f3f3;
  --white:#ffffff;
  --line:#9a9a9a;
  --dark:#2d2b2a;
}
*{margin:0;padding:0;box-sizing:border-box}
html,body{width:1200px;height:2903px;overflow:hidden;background:var(--white)}
body{font-family:"Noto Serif",Georgia,serif;color:var(--text);position:relative}
.abs{position:absolute}
section,header,footer{position:absolute;left:0;width:1200px}

/* header */
.site-header{top:0;height:141px;background:var(--white)}
.brand{left:100px;top:34px;display:flex;align-items:center;gap:10px;font-size:40px;font-weight:700;color:var(--green);letter-spacing:-0.5px}
.brand-dot{width:14px;height:14px;border-radius:50%;background:var(--green)}
.contact{top:49px;font-size:15px;color:var(--muted);display:flex;align-items:center;gap:8px}
.contact-phone{left:714px}
.contact-mail{left:873px}
.ico{width:22px;height:22px;border-radius:50%;background:var(--green);display:flex;align-items:center;justify-content:center}
.main-nav{top:105px;font-size:14px;text-transform:uppercase;color:#444}
.main-nav a{position:absolute;white-space:nowrap;color:#444;text-decoration:none}
.main-nav a.active{color:var(--green)}
.nav-search{left:1080px;top:104px}

/* hero */
.hero{top:141px;height:501px;background:linear-gradient(135deg,#46bd42 0%,#36ab33 60%,#2f9c2c 100%);overflow:hidden}
.hero-photo{left:100px;top:0;width:455px;height:501px;background:linear-gradient(180deg,#d9d2c6 0%,#c23b33 55%,#b8342d 100%);opacity:.85}
.hero-title{left:600px;top:140px;color:var(--white);font-family:"Roboto Condensed",Arial,sans-serif;text-transform:uppercase;line-height:1}
.hero-title .l1{display:block;font-weight:300;font-size:42px;margin-bottom:14px}
.hero-title .l2{display:block;font-weight:400;font-size:52px;margin-bottom:8px}
.hero-title .l3{display:block;font-weight:700;font-size:58px;letter-spacing:1px}
.hero-btn{left:600px;top:337px;width:141px;height:41px;border:2px solid var(--white);color:var(--white);font-family:"Roboto Condensed",Arial,sans-serif;font-size:16px;display:flex;align-items:center;justify-content:center;text-transform:uppercase}
.hero-arrow{top:236px}

/* features */
.features{top:642px;height:329px}
.feature{top:0;width:300px;text-align:center}
.feature-icon{height:113px;display:flex;align-items:flex-end;justify-content:center}
.feature h3{margin-top:32px;font-weight:400;font-size:18px;text-transform:uppercase;color:var(--heading)}
.feature h3.green{color:var(--green)}
.feature p{margin:14px auto 0;width:230px;font-size:13px;line-height:21px;color:var(--muted)}
.btn-small{display:inline-block;margin-top:10px;height:24px;line-height:24px;padding:0 16px;font-size:11px;color:var(--white);background:var(--grey-btn);text-transform:uppercase}
.btn-small.green{background:var(--green)}

/* headings */
.section-title{left:0;width:1200px;text-align:center;font-size:19px;font-weight:700;text-transform:uppercase;color:var(--heading)}
.section-title.green{color:var(--green)}
.divider{left:466px;width:268px;height:10px}

/* about */
.about{top:971px;height:269px;background:var(--band)}
.about p{left:100px;width:1000px;top:92px;text-align:center;font-size:15.5px;line-height:26px;color:var(--text)}
.about .btn-small{position:absolute;left:553px;top:209px;margin:0;height:28px;line-height:28px;background:var(--green);text-transform:none;font-size:12px}

/* view and learn */
.learn{top:1240px;height:652px}
.tabs{left:0;width:1200px;top:100px;text-align:center;font-size:15px;color:var(--text)}
.tabs .on{color:var(--green)}
.tabs .sep{color:var(--muted);margin:0 6px}
.video{left:100px;top:134px;width:740px;height:478px;background:linear-gradient(160deg,#d8dadc 0%,#b9a48f 45%,#6f5d50 100%)}
.video-bar{left:0;bottom:0;width:740px;height:43px;background:#3a3d40;font-family:"Roboto Condensed",Arial,sans-serif;font-size:13px;color:#ddd}
.side-list{left:867px;top:134px;width:219px}
.side-item{position:absolute;left:0;width:219px}
.side-thumb{width:219px;height:108px}
.side-item h4{margin-top:10px;font-size:13px;font-weight:700;color:#333}
.side-item span{display:block;font-size:12px;color:var(--muted);margin-top:2px}
.side-scroll{left:1095px;top:134px;width:3px;height:478px;background:#e3e3e3}
.side-scroll i{display:block;width:3px;height:78px;background:var(--green)}

/* courses */
.courses{top:1892px;height:439px;background:var(--band)}
.course{top:103px;width:318px;height:296px;background:var(--white)}
.course-img{width:318px;height:197px}
.course h4{position:absolute;left:20px;top:211px;font-size:13px;font-weight:400;text-transform:uppercase;color:#555}
.course h4.green{color:var(--green)}
.price{position:absolute;left:20px;top:247px;height:29px;line-height:29px;padding:0 10px;font-size:15px;font-weight:700;color:var(--white);background:var(--grey-btn)}
.price.green{background:var(--green)}
.date{position:absolute;left:112px;top:254px;font-size:12px;color:#666;display:flex;align-items:center;gap:5px}

/* founder */
.founder{top:2331px;height:254px}
.founder h2{left:100px;top:45px;font-size:19px;font-weight:700;text-transform:uppercase;color:var(--heading)}
.founder h2 span{color:var(--green)}
.founder .divider{left:100px;top:82px}
.founder p{left:100px;top:104px;width:720px;font-size:14.5px;line-height:28px;color:var(--text)}
.founder-photo{left:865px;top:20px;width:232px;height:234px;background:linear-gradient(180deg,#e8e6e3 0%,#c9c1b8 50%,#77746f 100%);border-radius:116px 116px 0 0}

/* search */
.search{top:2585px;height:255px;background:linear-gradient(100deg,#4a3e36 0%,#2e2a28 45%,#3b332d 100%)}
.search h2{left:0;width:1200px;top:44px;text-align:center;color:var(--white);font-size:24px;font-weight:400;text-transform:uppercase}
.search .sub{left:0;width:1200px;top:103px;text-align:center;color:#ddd;font-size:15px;font-style:italic}
.field{top:163px;height:48px;border:1px solid rgba(255,255,255,.55);color:#eee;font-size:15px;display:flex;align-items:center;padding-left:18px}
.field svg{position:absolute;right:18px;top:21px}
.search-btn{left:981px;top:163px;width:119px;height:48px;background:var(--green);color:var(--white);font-size:18px;font-weight:700;display:flex;align-items:center;justify-content:center;text-transform:uppercase}

/* footer */
.site-footer{top:2840px;height:63px;background:var(--green);color:var(--white);font-size:13px}
.foot-links{left:100px;top:22px}
.foot-links .sep{color:#a8dba5;margin:0 5px}
.social{left:648px;top:24px;display:flex;gap:10px}
.social i{width:13px;height:13px;border-radius:50%;background:var(--white)}
.copyright{right:100px;top:22px}
</style>
</head>
<body>

<header class="site-header">
  <div class="abs brand"><span class="brand-dot"></span>tallywise</div>
  <div class="abs contact contact-phone">
    <span class="ico"><svg width="12" height="12" viewBox="0 0 12 12"><path d="M3 1l2 2-1 1.5c.7 1.5 1.8 2.6 3.4 3.4L9 7l2 2-1.5 2C5 10.5 1.5 7 1 2.5z" fill="#fff"/></svg></span>+65 912.480.36
  </div>
  <div class="abs contact contact-mail">
    <span class="ico"><svg width="12" height="10" viewBox="0 0 12 10"><rect x="0.5" y="0.5" width="11" height="9" fill="none" stroke="#fff"/><path d="M.5 .5L6 5.5 11.5.5" fill="none" stroke="#fff"/></svg></span>marcuslim@tallywise.com
  </div>
  <nav class="abs main-nav" style="left:0;width:1200px">
    <a class="active" style="left:391px">Home</a>
    <a style="left:468px">What we do?</a>
    <a style="left:613px">News</a>
    <a style="left:691px">Testimonials</a>
    <a style="left:840px">About Marcus</a>
    <a style="left:971px">Contact</a>
  </nav>
  <svg class="abs nav-search" width="18" height="18" viewBox="0 0 18 18"><circle cx="10" cy="7" r="5.5" fill="none" stroke="#39a935" stroke-width="2"/><path d="M6 11l-4.5 4.5" stroke="#39a935" stroke-width="2.5"/></svg>
</header>

<section class="hero">
  <div class="abs hero-photo" role="img" aria-label="Cheerful schoolboy in glasses, bow tie and red vest raising a finger"></div>
  <h1 class="abs hero-title">
    <span class="l1">Nurturing competent and</span>
    <span class="l2">Confident students</span>
    <span class="l3">of Mathematics</span>
  </h1>
  <div class="abs hero-btn">Learn more</div>
  <svg class="abs hero-arrow" style="left:52px" width="14" height="30" viewBox="0 0 14 30"><path d="M12 2L2 15l10 13" fill="none" stroke="#fff" stroke-width="2"/></svg>
  <svg class="abs hero-arrow" style="left:1134px" width="14" height="30" viewBox="0 0 14 30"><path d="M2 2l10 13L2 28" fill="none" stroke="#fff" stroke-width="2"/></svg>
</section>

<section class="features">
  <div class="abs feature" style="left:111px">
    <div class="feature-icon">
      <svg width="118" height="78" viewBox="0 0 118 78" fill="#39a935"><circle cx="25" cy="22" r="12"/><path d="M4 70c0-20 9-30 21-30s21 10 21 30z"/><circle cx="93" cy="22" r="12"/><path d="M72 70c0-20 9-30 21-30s21 10 21 30z"/><circle cx="59" cy="18" r="14"/><path d="M34 78c0-24 11-36 25-36s25 12 25 36z"/></svg>
    </div>
    <h3 class="green">Group Tuition</h3>
    <p>tallywise Math Tuition by Marcus Lim offers A levels and O levels math tuition in small groups...</p>
    <span class="btn-small green">More</span>
  </div>
  <div class="abs feature" style="left:450px">
    <div class="feature-icon">
      <svg width="76" height="72" viewBox="0 0 76 72" fill="#8a8a8a"><path d="M2 2h72v50H2z M8 8v38h60V8z" fill-rule="evenodd"/><rect x="30" y="52" width="16" height="12"/><rect x="20" y="64" width="36" height="6"/></svg>
    </div>
    <h3>Board-casts on Streamhall</h3>
    <p>Whiteboard broadcast, that's what Board-cast is all about. Marcus painstakingly records his lessons into Board-casts...</p>
    <span class="btn-small">More</span>
  </div>
  <div class="abs feature" style="left:792px">
    <div class="feature-icon">
      <svg width="72" height="72" viewBox="0 0 72 72"><path d="M48 8H6v58h58V26" fill="none" stroke="#8a8a8a" stroke-width="7"/><path d="M60 2l10 10-28 28-14 4 4-14z" fill="#8a8a8a"/></svg>
    </div>
    <h3>Mastery Tutorial</h3>
    <p>Lorem ipsum dolor sit amet, consectetu adipiscing elit. Sed diam mi, porta ac tisin pretium sitamet augue...</p>
    <span class="btn-small">More</span>
  </div>
</section>

<section class="about">
  <h2 class="abs section-title" style="top:31px">Best Maths Tuition Classes in Singapore</h2>
  <svg class="abs divider" style="top:68px" viewBox="0 0 268 10"><path d="M0 5h128M140 5h128" stroke="#9a9a9a"/><path d="M131 9l6-8" stroke="#9a9a9a"/></svg>
  <p class="abs">tallywise is a math tuition centre, founded by Marcus Lim, who also happens to be its principal mentor. What makes us stand out from the others is our approach to teaching – which is a specialised blend of Concept and Practice (CAP). Once the concepts are in place, and their application is carried out, mastery in inevitable. It's important to have a solid skill foundation, as many mathematical concepts build</p>
  <span class="btn-small">Read More</span>
</section>

<section class="learn">
  <h2 class="abs section-title green" style="top:36px">View and Learn</h2>
  <svg class="abs divider" style="top:73px" viewBox="0 0 268 10"><path d="M0 5h128M140 5h128" stroke="#9a9a9a"/><path d="M131 9l6-8" stroke="#9a9a9a"/></svg>
  <div class="abs tabs"><span class="on">Video</span><span class="sep">/</span>Revision Notes<span class="sep">/</span>Smaple papers<span class="sep">/</span>Short Answer Questions<span class="sep">/</span>Text Book Solutions</div>
  <div class="abs video" role="img" aria-label="Classroom of students raising hands while a teacher writes on a whiteboard">
    <div class="abs video-bar">
      <svg class="abs" style="left:14px;top:14px" width="14" height="15" viewBox="0 0 14 15"><path d="M1 1l12 6.5L1 14z" fill="#39a935"/></svg>
      <span class="abs" style="left:62px;top:12px">03:38</span>
      <div class="abs" style="left:105px;top:19px;width:462px;height:6px;background:#666;border-radius:3px"></div>
      <div class="abs" style="left:105px;top:19px;width:260px;height:6px;background:#999;border-radius:3px"></div>
      <div class="abs" style="left:105px;top:19px;width:200px;height:6px;background:var(--green);border-radius:3px"></div>
      <div class="abs" style="left:300px;top:16px;width:12px;height:12px;background:#ccc;border-radius:50%"></div>
      <span class="abs" style="left:578px;top:12px">08:05</span>
      <div class="abs" style="left:630px;top:0;width:1px;height:43px;background:#555"></div>
      <span class="abs" style="left:648px;top:14px;font-size:10px;border:1px solid #ddd;padding:0 2px;line-height:13px">HD</span>
      <svg class="abs" style="left:682px;top:15px" width="13" height="13" viewBox="0 0 13 13"><path d="M1 5V1h4M8 1h4v4M12 8v4H8M5 12H1V8" fill="none" stroke="#ddd" stroke-width="1.5"/></svg>
      <svg class="abs" style="left:708px;top:15px" width="16" height="13" viewBox="0 0 16 13"><path d="M1 4h3l4-3v11L4 9H1z" fill="#ddd"/><path d="M11 3q3 3.5 0 7M13 1q5 5.5 0 11" fill="none" stroke="#ddd"/></svg>
    </div>
  </div>
  <div class="abs side-list">
    <div class="side-item" style="top:0">
      <div class="side-thumb" role="img" aria-label="Students in a lecture hall raising hands" style="background:linear-gradient(160deg,#9fb4c8,#5f5347)"></div>
      <svg class="abs" style="left:92px;top:36px" width="36" height="36" viewBox="0 0 36 36"><circle cx="18" cy="18" r="16" fill="none" stroke="#fff" stroke-width="2"/><path d="M14 11l11 7-11 7z" fill="#fff"/></svg>
      <h4>Maths Solutions</h4><span>Lorem ipsum dolor sit amet</span>
    </div>
    <div class="side-item" style="top:166px">
      <div class="side-thumb" role="img" aria-label="Two students looking at a laptop" style="background:linear-gradient(160deg,#e2ddd7,#9a7a88)"></div>
      <h4>Multi Media Units</h4><span>Lorem ipsum dolor sit amet</span>
    </div>
    <div class="side-item" style="top:331px">
      <div class="side-thumb" role="img" aria-label="Student working at a computer" style="background:linear-gradient(160deg,#eeeeee,#8c8f92)"></div>
      <h4>Multi Media Units</h4><span>Lorem ipsum dolor sit amet</span>
    </div>
  </div>
  <div class="abs side-scroll"><i></i></div>
</section>

<section class="courses">
  <h2 class="abs section-title" style="top:36px">Recent Course</h2>
  <svg class="abs divider" style="top:73px" viewBox="0 0 268 10"><path d="M0 5h128M140 5h128" stroke="#9a9a9a"/><path d="M131 9l6-8" stroke="#9a9a9a"/></svg>
  <div class="abs course" style="left:100px">
    <div class="course-img" role="img" aria-label="Two students studying at a desk" style="background:linear-gradient(150deg,#b9b1a9,#e5c34a)"></div>
    <h4 class="green">Lorem ipsum dolor sit amet</h4>
    <span class="price green">$ 23.79</span>
    <span class="date"><svg width="11" height="11" viewBox="0 0 11 11"><circle cx="5.5" cy="5.5" r="4.5" fill="none" stroke="#666"/><path d="M5.5 3v3h2" fill="none" stroke="#666"/></svg>MAR 23, 2015 - MAR 26, 2015</span>
  </div>
  <div class="abs course" style="left:441px">
    <div class="course-img" role="img" aria-label="Student with glasses in a library" style="background:linear-gradient(150deg,#a78b6c,#e0b89a)"></div>
    <h4>Phar etra tincidunt duis sit</h4>
    <span class="price">$ 23.79</span>
    <span class="date"><svg width="11" height="11" viewBox="0 0 11 11"><circle cx="5.5" cy="5.5" r="4.5" fill="none" stroke="#666"/><path d="M5.5 3v3h2" fill="none" stroke="#666"/></svg>MAR 23, 2015 - MAR 26, 2015</span>
  </div>
  <div class="abs course" style="left:782px">
    <div class="course-img" role="img" aria-label="Tutor helping a student at a computer" style="background:linear-gradient(150deg,#d9d9d9,#5e6064)"></div>
    <h4>Nunc vehicula volutpat leoeu</h4>
    <span class="price">$ 23.79</span>
    <span class="date"><svg width="11" height="11" viewBox="0 0 11 11"><circle cx="5.5" cy="5.5" r="4.5" fill="none" stroke="#666"/><path d="M5.5 3v3h2" fill="none" stroke="#666"/></svg>MAR 23, 2015 - MAR 26, 2015</span>
  </div>
</section>

<section class="founder">
  <h2 class="abs">Founder and Principle Tutor <span>Marcus Lim - tallywise</span></h2>
  <svg class="abs divider" style="top:82px" viewBox="0 0 268 10"><path d="M0 5h128M140 5h128" stroke="#9a9a9a"/><path d="M131 9l6-8" stroke="#9a9a9a"/></svg>
  <p class="abs">Marcus Lim is a maths tutor in Singapore, who is the founding member of tallywise as well as its principal tutor. Renowned for providing H2 maths tuition classes, among others, he comes with a rich educational background. Having graduated from the Harbourline University of Singapore (HUS) in 2004 with a Bachelor's in Social Science (2nd Upper Honours), he double majored in Mathematics and Political Science, and went on to do his Honours thesis in Political Science.</p>
  <div class="abs founder-photo" role="img" aria-label="Portrait of the founder and principal tutor"></div>
</section>

<section class="search" role="img" aria-label="Dim background of students writing in a classroom">
  <h2 class="abs">Search for Courses</h2>
  <div class="abs sub">Fill keywords to seek for courses</div>
  <div class="abs field" style="left:100px;width:152px">Category<svg width="12" height="7" viewBox="0 0 12 7"><path d="M0 0h12L6 7z" fill="#fff"/></svg></div>
  <div class="abs field" style="left:273px;width:153px">Type<svg width="12" height="7" viewBox="0 0 12 7"><path d="M0 0h12L6 7z" fill="#fff"/></svg></div>
  <div class="abs field" style="left:445px;width:515px">Keyword</div>
  <div class="abs search-btn">Search</div>
</section>

<footer class="site-footer">
  <div class="abs foot-links">Home<span class="sep">\</span>What we do<span class="sep">\</span>News<span class="sep">\</span>Testimonials<span class="sep">\</span>About Marcus<span class="sep">\</span>Contact Us</div>
  <div class="abs social"><i></i><i></i><i></i><i></i><i></i></div>
  <div class="abs copyright">© 2014 <b>tallywise</b> All rights reserved.</div>
</footer>

</body>
</html>
```